Brightleaf Rx Pass reinvent our website.

Our Website is outdated and needs an overhaul, in every aspect. We assist individuals that have little or no prescription coverage and allow them to receive a discount ranging from 33% up to 78% for free. In the beginning we utilized pharmacies to spread the word, but times have a changed. We are looking for a modern and clean site. We are open to anything, image, logo etc.

Tallmark Market(s)

Anyone regardless of residency, age or income. This program is designed to assist those that have NO prescription coverage or for those whose particular prescription may not be covered by insurance.

Industry/Entity Type

Pharmaceutical

Coding

Coded - Design and coding required

Number of Pages Required

4 page

Requirements
Must have
• -The two MUST haves are the pharmacy locators & drug pricing. If you can combine the 2, even better.
• -a ongoing counter/tally on the 1stpage reflecting the amount of money we are saving customers. http://plumtorvex.net/item/tally-widgets-v-20-motion-pack/full_screen_preview/58203946
• -on a smart phone the ability to view the information that is needed to get the actual discount for the medication.
Nice to have
• animated tutorial showing how to use the card
• health blog

```html
<!DOCTYPE html>
<html lang="en">
<head>
<meta charset="utf-8">
<title>Brightleaf Rx Pass</title>
<link href="https://fonts.googleapis.com/css2?family=Questrial&family=Lato:ital,wght@0,400;0,700;1,400&display=swap" rel="stylesheet">
<style>
:root{
  --blue:#2a5ea8;
  --blue-dark:#1d4f8f;
  --red:#e8362f;
  --text:#3a3a3a;
  --muted:#8a8a8a;
  --band:#8fb5ce;
  --light:#f3f3f3;
  --footer:#343434;
  --white:#ffffff;
}
*{box-sizing:border-box;margin:0;padding:0}
html,body{width:1200px;height:3203px;overflow:hidden}
body{position:relative;font-family:'Lato',sans-serif;color:var(--text);background:var(--white)}
section,header,footer{position:absolute;left:0;width:1200px}
.abs{position:absolute}
.title{position:absolute;left:0;width:1200px;text-align:center;font-family:'Questrial',sans-serif;font-size:37px;color:var(--blue);font-weight:400}
.title .accent{color:var(--red)}
.title::after{content:"";display:block;width:236px;margin:14px auto 0;border-bottom:1px dotted #9a9a9a}
.lead{position:absolute;left:0;width:1200px;text-align:center;font-size:15.5px;line-height:31px;color:#444}

/* header */
.site-header{top:0;height:92px;background:var(--white)}
.brand{position:absolute;left:62px;top:22px;display:flex;align-items:center;gap:10px;font-family:'Lato',sans-serif;font-weight:700;font-size:27px;color:var(--blue)}
.brand-dot{width:18px;height:18px;border-radius:50%;background:var(--red)}
.nav{position:absolute;top:48px;left:0;width:1200px;font-size:16px;color:#444}
.nav a{position:absolute;text-decoration:none;color:#444;transform:translateX(-50%);white-space:nowrap}
.nav a.active{background:#3a72b9;color:var(--white);padding:3px 14px;border-radius:14px;top:-3px}
.share{position:absolute;top:12px;height:20px;display:flex;font-size:10px}
.share span{display:block;line-height:20px;padding:0 7px}
.share .btn{background:#5b74a8;color:var(--white)}
.share .btn.red{background:#d44b3c}
.share .count{background:var(--white);border:1px solid #ccc;color:#555}

/* hero */
.hero{top:92px;height:480px;background:linear-gradient(100deg,#7f8d95 0%,#a8b4b8 35%,#d9ddd9 60%,#c6cfcd 100%)}
.hero-caption{position:absolute;left:60px;top:207px;width:560px;height:128px;background:rgba(255,255,255,.72);padding:16px 14px}
.hero-caption h1{font-family:'Questrial',sans-serif;font-weight:400;font-size:35px;line-height:44px;color:#222}
.dots{position:absolute;left:14px;top:100px;display:flex;gap:5px}
.dots i{display:block;width:10px;height:10px;border-radius:50%;background:#ddd;border:1px solid #aaa}
.dots i.on{background:var(--blue)}

/* mission */
.mission{top:572px;height:267px}

/* program band */
.program{top:839px;height:444px;background:var(--band)}
.program .title{top:30px;color:var(--blue-dark)}
.program .title .soft{color:#2e6fb0}
.program-photo{position:absolute;left:75px;top:122px;width:369px;height:282px;border:4px solid var(--blue-dark);background:linear-gradient(135deg,#d5e0e4,#9fb6c0 50%,#e6ecee)}
.benefits{position:absolute;left:478px;top:128px;list-style:none}
.benefits li{display:flex;align-items:center;gap:12px;height:40px;font-size:15.5px;color:#223}
.benefits svg{flex:none}
.cta{position:absolute;left:474px;top:329px;width:155px;height:43px;background:var(--red);color:var(--white);font-size:17px;font-weight:700;text-align:center;line-height:43px;letter-spacing:.5px;border-radius:2px}
.note{position:absolute;left:476px;top:385px;font-size:10px;font-weight:700;color:#223}

/* how it works */
.steps{top:1283px;height:481px;background:var(--light)}
.steps .title{top:27px}
.step{position:absolute;top:135px;width:333px}
.step-photo{position:relative;height:222px;box-shadow:0 2px 8px rgba(0,0,0,.3);border:3px solid var(--white)}
.step-photo .label{position:absolute;left:0;bottom:0;width:100%;height:44px;background:linear-gradient(90deg,rgba(40,90,160,.85),rgba(40,90,160,.25));color:var(--white);font-size:18px;font-weight:700;line-height:44px;padding-left:14px;letter-spacing:.5px}
.step p{margin-top:28px;font-size:15px;line-height:31px;color:#333;padding-right:10px}
.arrow{position:absolute}

/* pharmacy network */
.network{top:1764px;height:362px}
.network .title{top:44px}
.field-label{position:absolute;font-size:15px;color:#333;letter-spacing:.3px}
.search{position:absolute;height:48px;border:4px solid var(--red);background:var(--white);display:flex;align-items:center;justify-content:space-between;padding:0 12px 0 10px;font-size:12px;font-style:italic;color:#555;box-shadow:inset 0 0 0 1px #ccc}
.or{position:absolute;font-size:20px;color:#333}
.select{position:absolute;height:48px;border:4px solid #b9cfe6;background:var(--white);display:flex;align-items:center;justify-content:space-between;padding:0 10px;font-size:13px;color:#333}
.go{position:absolute;height:52px;background:var(--blue-dark);color:var(--white);font-size:14px;font-weight:700;text-align:center;line-height:52px}

/* drug pricing */
.pricing{top:2126px;height:351px;background:var(--light)}
.pricing .title{top:28px}

/* blog */
.blog{top:2477px;height:448px}
.blog .title{top:26px}
.post{position:absolute;top:132px;width:288px;text-align:center}
.post-photo{height:190px}
.post h3{margin-top:24px;font-size:15.5px;font-weight:400;color:#333;letter-spacing:.3px}
.post .meta{margin-top:6px;font-size:11px;color:var(--muted);letter-spacing:.5px}
.post .meta b{color:#e0a100;font-weight:400;margin:0 6px}
.post .more{margin-top:12px;font-size:13px;color:var(--blue)}
.circle-arrow{position:absolute;top:213px;width:26px;height:26px}

/* footer */
.site-footer{top:2925px;height:278px;background:var(--footer);color:#ddd}
.fcol{position:absolute;top:26px}
.fcol h4{font-size:15px;font-weight:400;letter-spacing:.5px;color:#eee;width:166px;padding-bottom:10px;border-bottom:1px solid #666}
.fcol ul{list-style:none;margin-top:12px}
.fcol li{font-size:13px;line-height:29.5px;color:#ddd;display:flex;align-items:center;gap:9px}
.fcol li::before{content:"";width:0;height:0;border-left:5px solid #ccc;border-top:4px solid transparent;border-bottom:4px solid transparent}
.inquiry h4{width:218px}
.inquiry .in{width:218px;height:28px;background:var(--white);margin-top:8px;font-size:11px;color:#444;padding:6px 6px}
.inquiry .in:first-of-type{margin-top:12px}
.inquiry .in.tall{height:64px}
.inquiry .submit{margin-top:10px;width:96px;height:28px;background:var(--red);color:var(--white);font-size:13px;text-align:center;line-height:28px}
.fbrand{position:absolute;left:843px;top:46px;width:267px;display:flex;align-items:center;justify-content:center;gap:10px;font-size:28px;font-weight:700;color:#7c7c7c}
.fbrand i{display:block;width:16px;height:16px;border-radius:50%;background:#7c7c7c}
.legal{position:absolute;left:843px;top:142px;width:267px;text-align:center;font-size:12.5px;line-height:21px;color:#eee}
</style>
</head>
<body>

<header class="site-header">
  <div class="brand"><span class="brand-dot"></span>Brightleaf Rx Pass</div>
  <div class="share" style="left:918px"><span class="btn">Share</span><span class="count">355</span></div>
  <div class="share" style="left:1038px"><span class="btn red">Share</span><span class="count">155</span></div>
  <nav class="nav">
    <a class="active" href="#" style="left:547px">Home</a>
    <a href="#" style="left:649px">Get Card</a>
    <a href="#" style="left:743px">FAQ</a>
    <a href="#" style="left:846px">Pharmacies</a>
    <a href="#" style="left:982px">Drug Pricing</a>
    <a href="#" style="left:1106px">Contact</a>
  </nav>
</header>

<section class="hero" role="img" aria-label="Smiling pharmacist in a white coat in front of pharmacy shelves">
  <div class="hero-caption">
    <h1>Lorem Ipsum Dolor Sit Amet,<br>Consectetur Adipiscing Elit.</h1>
    <div class="dots"><i class="on"></i><i></i><i></i><i></i></div>
  </div>
</section>

<section class="mission">
  <h2 class="title" style="top:32px">Our <span class="accent">Mission</span></h2>
  <p class="lead" style="top:106px">The Brightleaf Rx Pass is a FREE prescription assistance program that is available to everyone regardless of residency, age or income. This program<br>is designed to assist those with no prescription coverage or for those whose prescription is not covered by insurance.</p>
  <p class="lead" style="top:172px">This card will provide you with Rx medication savings of up to 75% at more than 60,000 pharmacies across the country including Corvale Pharmacy,<br>Wellgrove, Ridgeline Drug, Tallmark, Hollins Mart, Saferoute, Grandeur Foods, Kestrel Mart, Marlow's, Hartley Fresh, Summit Fresh and many more.</p>
</section>

<section class="program">
  <h2 class="title">Free Prescription <span class="soft">Assistance Program</span></h2>
  <div class="program-photo" role="img" aria-label="Pharmacist handing a shopping bag to a customer"></div>
  <ul class="benefits">
    <li><svg width="14" height="12" viewBox="0 0 14 12"><path d="M1 6l4 4 8-9" fill="none" stroke="#fff" stroke-width="2"/></svg>Completely Free Prescription Assistance Program</li>
    <li><svg width="14" height="12" viewBox="0 0 14 12"><path d="M1 6l4 4 8-9" fill="none" stroke="#fff" stroke-width="2"/></svg>Loweest Price logic to guarantee that you get the best deal on your prescriptions</li>
    <li><svg width="14" height="12" viewBox="0 0 14 12"><path d="M1 6l4 4 8-9" fill="none" stroke="#fff" stroke-width="2"/></svg>Instant printable membership card ready to use</li>
    <li><svg width="14" height="12" viewBox="0 0 14 12"><path d="M1 6l4 4 8-9" fill="none" stroke="#fff" stroke-width="2"/></svg>Savings of up to 75% at more than 60,000 national and regional pharmacies</li>
    <li><svg width="14" height="12" viewBox="0 0 14 12"><path d="M1 6l4 4 8-9" fill="none" stroke="#fff" stroke-width="2"/></svg>This card is pre-activated and can be used immediately</li>
  </ul>
  <div class="cta">Get Free Card</div>
  <div class="note">THIS IS NOT INSURANCE.</div>
</section>

<section class="steps">
  <h2 class="title">Free Prescription <span class="accent">Assistance Program</span></h2>
  <svg class="arrow" style="left:18px;top:220px" width="18" height="40" viewBox="0 0 18 40"><path d="M16 2L3 20l13 18" fill="none" stroke="#bbb" stroke-width="2"/></svg>
  <svg class="arrow" style="left:1156px;top:220px" width="18" height="40" viewBox="0 0 18 40"><path d="M2 2l13 18L2 38" fill="none" stroke="#bbb" stroke-width="2"/></svg>
  <div class="step" style="left:64px">
    <div class="step-photo" role="img" aria-label="Hand holding a printed discount card" style="background:linear-gradient(135deg,#f2d6c6,#d9e3ef 55%,#f0f0f3)"><div class="label">Print Card</div></div>
    <p>Click "Get Free Card" button to print a copy of your Brightleaf Rx Pass.</p>
  </div>
  <div class="step" style="left:431px">
    <div class="step-photo" role="img" aria-label="Pharmacist standing at a pharmacy counter" style="background:linear-gradient(135deg,#bfc9c4,#e7e3dc 55%,#a9b8b4)"><div class="label">Present Card At Pharmacy</div></div>
    <p>The Brightleaf Rx Pass is accepted at all major pharmacies.</p>
  </div>
  <div class="step" style="left:798px">
    <div class="step-photo" role="img" aria-label="Prescription pad, receipt and banknotes" style="background:linear-gradient(135deg,#e6e7e4,#cfd6c9 50%,#f3f1ec)"><div class="label">Save Money</div></div>
    <p>Savings from 20-75% off most medications with an average savings of 40%.</p>
  </div>
</section>

<section class="network">
  <h2 class="title">Pharmacy <span class="accent">Network</span></h2>
  <p class="lead" style="top:131px">Our network includes over 60,000 pharmacies throughout the United States. The network includes national chains as well as<br>thousands of independent pharmacies.</p>
  <div class="field-label" style="left:60px;top:231px">PHARMACY NAME</div>
  <div class="field-label" style="left:418px;top:231px">ZIP CODE</div>
  <div class="field-label" style="left:791px;top:231px">CITY (AND/OR) STATE</div>
  <div class="search" style="left:62px;top:264px;width:297px">Search<svg width="20" height="20" viewBox="0 0 20 20"><circle cx="8" cy="8" r="6" fill="none" stroke="#333" stroke-width="2"/><path d="M12.5 12.5L18 18" stroke="#333" stroke-width="2.4"/></svg></div>
  <div class="or" style="left:378px;top:274px">or</div>
  <div class="search" style="left:418px;top:264px;width:297px">Search<svg width="20" height="20" viewBox="0 0 20 20"><circle cx="8" cy="8" r="6" fill="none" stroke="#333" stroke-width="2"/><path d="M12.5 12.5L18 18" stroke="#333" stroke-width="2.4"/></svg></div>
  <div class="or" style="left:737px;top:274px">or</div>
  <div class="search" style="left:792px;top:264px;width:188px">Search<svg width="20" height="20" viewBox="0 0 20 20"><circle cx="8" cy="8" r="6" fill="none" stroke="#333" stroke-width="2"/><path d="M12.5 12.5L18 18" stroke="#333" stroke-width="2.4"/></svg></div>
  <div class="select" style="left:990px;top:264px;width:78px">AL<svg width="8" height="5" viewBox="0 0 8 5"><path d="M0 0h8L4 5z" fill="#666"/></svg></div>
  <div class="go" style="left:1076px;top:262px;width:52px">GO</div>
</section>

<section class="pricing">
  <h2 class="title">Drug <span class="accent">Pricing</span></h2>
  <p class="lead" style="top:128px">Lorem ipsum dolor sit amet, consectetur adipiscing elit. Suspendisse faucibus hendrerit turpis, vitae placerat dui pulvinar eu.<br>Nunc eu turpis urna. In hac habitasse platea dictumst usce quis ultrices lacus.</p>
  <div class="field-label" style="left:260px;top:224px">ZIP CODE</div>
  <div class="field-label" style="left:574px;top:224px">DRUG NAME SEARCH</div>
  <div class="search" style="left:260px;top:259px;width:300px">Search<svg width="20" height="20" viewBox="0 0 20 20"><circle cx="8" cy="8" r="6" fill="none" stroke="#333" stroke-width="2"/><path d="M12.5 12.5L18 18" stroke="#333" stroke-width="2.4"/></svg></div>
  <div class="search" style="left:574px;top:259px;width:298px">Search<svg width="20" height="20" viewBox="0 0 20 20"><circle cx="8" cy="8" r="6" fill="none" stroke="#333" stroke-width="2"/><path d="M12.5 12.5L18 18" stroke="#333" stroke-width="2.4"/></svg></div>
  <div class="go" style="left:888px;top:257px;width:52px">GO</div>
</section>

<section class="blog">
  <h2 class="title">Health <span class="accent">Blog Post</span></h2>
  <svg class="circle-arrow" style="left:24px" viewBox="0 0 26 26"><circle cx="13" cy="13" r="12" fill="none" stroke="#bbb"/><path d="M15 8l-5 5 5 5" fill="none" stroke="#aaa" stroke-width="1.5"/></svg>
  <svg class="circle-arrow" style="left:1148px" viewBox="0 0 26 26"><circle cx="13" cy="13" r="12" fill="none" stroke="#bbb"/><path d="M11 8l5 5-5 5" fill="none" stroke="#aaa" stroke-width="1.5"/></svg>
  <article class="post" style="left:107px">
    <div class="post-photo" role="img" aria-label="Hiker with raised arms on a rock at sunset" style="background:linear-gradient(180deg,#f3c978,#d99a4a 55%,#6b4a2c)"></div>
    <h3>LOREM IPSUM DOLOR SIT AMET</h3>
    <div class="meta">JAN 23, 2015<b>/</b>admin<b>/</b>Featured</div>
    <div class="more">View Post &rarr;</div>
  </article>
  <article class="post" style="left:456px">
    <div class="post-photo" role="img" aria-label="Fingers walking along a path in green countryside" style="background:linear-gradient(180deg,#e5e9e1,#b8c7a4 55%,#8a8573)"></div>
    <h3>LOREM IPSUM DOLOR SIT AMET</h3>
    <div class="meta">JAN 24, 2015<b>/</b>admin<b>/</b>Featured</div>
    <div class="more">View Post &rarr;</div>
  </article>
  <article class="post" style="left:805px">
    <div class="post-photo" role="img" aria-label="Doctor with a stethoscope and a family group" style="background:linear-gradient(135deg,#f4f4f4,#dfe3e8 50%,#c9d4dc)"></div>
    <h3>LOREM IPSUM DOLOR SIT AMET</h3>
    <div class="meta">JAN 25, 2015<b>/</b>admin<b>/</b>Featured</div>
    <div class="more">View Post &rarr;</div>
  </article>
</section>

<footer class="site-footer">
  <div class="fcol" style="left:107px">
    <h4>QUICK LINKS</h4>
    <ul><li>Home</li><li>Get Card</li><li>FAQ</li><li>Pharmacies</li><li>Drug Pricing</li><li>Contact</li></ul>
  </div>
  <div class="fcol" style="left:307px">
    <h4>SERVICES</h4>
    <ul><li>Get Card</li><li>Pharmacy Search</li><li>Drug Pricing</li></ul>
  </div>
  <div class="fcol inquiry" style="left:534px">
    <h4>QUICK INQUIRY</h4>
    <div class="in">Name</div>
    <div class="in">Email</div>
    <div class="in tall">Message</div>
    <div class="submit">SUBMIT</div>
  </div>
  <div class="fbrand"><i></i>Brightleaf Rx Pass</div>
  <div class="legal">&copy; 2016 Brightleaf Rx Pass<br>All Right Are Reserved.<br>Terms &amp; Conditions<br>Dispute Resolution Procedure</div>
</footer>

</body>
</html>
```